Flyer Advertisement Simple But Creative

Flyer dimensions 4" x 6"

Simple design with logo and additional info. On the front of the flyer:

- place the logo at the top
- beneath the logo add the website and phone number
- simple less is more approach
- feel free to add your own personal touch

On the back:

- Requirements
- Perfect for Birthdays and Anniversaries
- Rentals available hourly, daily, and weekly
- Group Rentals available at discounted rates
- Enter to win a free rental - url and QR code

Industry/Entity Type

Car Rental

Font styles to use
Serif
Sans Serif

Colors

Designer to choose colors to be used in the design.

Requirements
Must have
• FRONT:
• Please include our phone number and website:
• 614-287-3951
• www.BrindlewoodTrikeHire.example
• BACK:
• REQUIREMENTS
• At least 25 years of age
• Valid Driver's License
• Debit or Credit Card
• Must know how to drive a manual transmission or stick shift

```html
<!DOCTYPE html>
<html lang="en">
<head>
<meta charset="utf-8">
<title>Brindlewood Trike Hire – Flyer Front and Back</title>
<link rel="stylesheet" href="https://fonts.googleapis.com/css2?family=Roboto+Slab:wght@700&family=Source+Serif+4:wght@400;600&display=swap">
<style>
  :root {
    --stage: #8e8e8e;
    --ink: #14181b;
    --ink-soft: #22282c;
    --paper: #f4f4f4;
    --accent: #e8174a;
    --ring: #5b6064;
    --text-light: #f1f1f1;
  }
  * { margin: 0; padding: 0; box-sizing: border-box; }
  html, body {
    width: 1200px; height: 850px; overflow: hidden;
    background: var(--stage);
  }
  .stage {
    position: relative; width: 1200px; height: 850px;
    display: flex; justify-content: center; align-items: center; gap: 80px;
  }
  .flyer {
    position: relative; width: 480px; height: 720px; overflow: hidden;
    background: var(--ink);
    box-shadow: 0 10px 30px rgba(0,0,0,.25);
  }
  .flyer-art { position: absolute; inset: 0; width: 480px; height: 720px; }

  .brand-name {
    position: absolute; left: 250px; top: 78px; width: 170px;
    text-align: center;
    font-family: "Source Serif 4", Georgia, serif; font-weight: 600;
    font-size: 19px; line-height: 1.15; color: var(--ink);
  }

  .contact-bar {
    position: absolute; left: 38px; top: 660px; width: 404px; height: 34px;
    background: var(--accent);
    display: flex; align-items: center; justify-content: center; gap: 10px;
    font-family: "Source Serif 4", Georgia, serif; font-size: 14px;
    color: #fff; white-space: nowrap;
  }
  .contact-bar .divider { opacity: .9; }

  .requirements {
    position: absolute; left: 262px; top: 318px; width: 200px;
    font-family: "Source Serif 4", Georgia, serif; color: var(--text-light);
  }
  .requirements h2 {
    font-family: "Roboto Slab", Georgia, serif; font-weight: 700;
    font-size: 17px; letter-spacing: .5px; color: var(--accent);
    margin-bottom: 6px;
  }
  .requirements ul { list-style: none; font-size: 13.5px; line-height: 1.45; }
</style>
</head>
<body>
<main class="stage">

  <!-- Front of flyer -->
  <section class="flyer flyer-front">
    <svg class="flyer-art" viewBox="0 0 480 720" xmlns="http://www.w3.org/2000/svg">
      <defs>
        <linearGradient id="heroTrike" x1="0" y1="0" x2="1" y2="1">
          <stop offset="0" stop-color="#b9b6b0"/>
          <stop offset=".5" stop-color="#b8202e"/>
          <stop offset="1" stop-color="#3a3a3c"/>
        </linearGradient>
        <linearGradient id="silverTrike" x1="0" y1="0" x2="0" y2="1">
          <stop offset="0" stop-color="#e6e8ea"/>
          <stop offset="1" stop-color="#6e7174"/>
        </linearGradient>
        <linearGradient id="garageTrike" x1="0" y1="0" x2="0" y2="1">
          <stop offset="0" stop-color="#9a8a70"/>
          <stop offset=".6" stop-color="#2b3238"/>
          <stop offset="1" stop-color="#1a2a36"/>
        </linearGradient>
      </defs>
      <rect class="backdrop" width="480" height="720" fill="#14181b"/>
      <path class="backdrop-swirl" d="M120,420 C260,320 420,380 480,300 L480,720 L0,720 Z" fill="#1c2226"/>

      <circle class="logo-panel" cx="330" cy="-40" r="200" fill="#f4f4f4"/>
      <circle class="logo-panel-edge" cx="330" cy="-40" r="208" fill="none" stroke="#e8174a" stroke-width="4"/>

      <circle class="hero-ring" cx="115" cy="205" r="196" fill="#e8174a"/>
      <g role="img" aria-label="Photo of a red three-wheeled roadster parked outdoors">
        <circle cx="115" cy="205" r="180" fill="url(#heroTrike)"/>
      </g>

      <circle class="thumb-ring" cx="365" cy="330" r="88" fill="#5b6064"/>
      <g role="img" aria-label="Photo of a silver three-wheeled roadster, front view">
        <circle cx="365" cy="330" r="78" fill="url(#silverTrike)"/>
      </g>
      <circle cx="365" cy="330" r="68" fill="none" stroke="#e8174a" stroke-width="1.2"/>

      <path class="bottom-panel" d="M480,430 C470,600 300,690 0,705 L0,720 L480,720 Z" fill="#f4f4f4"/>
      <path class="bottom-line" d="M470,440 C455,600 290,680 0,692" fill="none" stroke="#e8174a" stroke-width="1.5"/>

      <circle class="thumb-ring" cx="215" cy="520" r="102" fill="#5b6064"/>
      <g role="img" aria-label="Photo of a roadster with blue wheel lights in a garage">
        <circle cx="215" cy="520" r="92" fill="url(#garageTrike)"/>
      </g>
      <circle cx="215" cy="520" r="82" fill="none" stroke="#e8174a" stroke-width="1.2"/>
    </svg>

    <p class="brand-name">Brindlewood Trike Hire</p>

    <p class="contact-bar">
      <span class="phone">T : 614-287-3951</span>
      <span class="divider">|</span>
      <span class="web">W : www.BrindlewoodTrikeHire.example</span>
    </p>
  </section>

  <!-- Back of flyer -->
  <section class="flyer flyer-back">
    <svg class="flyer-art" viewBox="0 0 480 720" xmlns="http://www.w3.org/2000/svg">
      <defs>
        <linearGradient id="cockpit" x1="0" y1="0" x2="1" y2="1">
          <stop offset="0" stop-color="#d9d9d9"/>
          <stop offset=".4" stop-color="#2c2f33"/>
          <stop offset=".7" stop-color="#a0202c"/>
          <stop offset="1" stop-color="#1b1d20"/>
        </linearGradient>
        <linearGradient id="greenTrike" x1="0" y1="0" x2="0" y2="1">
          <stop offset="0" stop-color="#e9ecee"/>
          <stop offset=".6" stop-color="#7d8286"/>
          <stop offset="1" stop-color="#c9d36a"/>
        </linearGradient>
      </defs>
      <rect class="backdrop" width="480" height="720" fill="#14181b"/>
      <path class="backdrop-swirl" d="M0,430 C160,360 360,420 480,330 L480,720 L0,720 Z" fill="#1c2226"/>

      <circle class="hero-ring" cx="140" cy="170" r="215" fill="#5b6064"/>
      <g role="img" aria-label="Photo of the roadster cockpit with steering wheel and dashboard">
        <circle cx="140" cy="170" r="200" fill="url(#cockpit)"/>
      </g>

      <path class="bottom-panel" d="M480,470 C430,620 260,700 0,710 L0,720 L480,720 Z" fill="#f4f4f4"/>
      <path class="bottom-line" d="M470,455 C420,610 250,688 0,698" fill="none" stroke="#e8174a" stroke-width="1.5"/>

      <circle class="thumb-ring" cx="345" cy="575" r="90" fill="#f4f4f4"/>
      <g role="img" aria-label="Photo of a white and lime three-wheeled roadster, front view">
        <circle cx="345" cy="575" r="82" fill="url(#greenTrike)"/>
      </g>
      <circle cx="345" cy="575" r="90" fill="none" stroke="#e8174a" stroke-width="1.2" stroke-dasharray="3 3"/>
    </svg>

    <div class="requirements">
      <h2>REQUIREMENTS</h2>
      <ul>
        <li>At least 25 years of age</li>
        <li>Valid Driver's License</li>
        <li>Debit or Credit Card</li>
        <li>Must know how to drive a manual transmission or stick shift</li>
      </ul>
    </div>
  </section>

</main>
</body>
</html>
```